Brindlecove Ventures Co. requiresupdated PPT Master

We are a software company that specializes in Business Management solutions for the global Oil and Gas sector. We have an existing logo and color scheme but we would like a new modern twist for our PPT Master template. We would like it to be simple and clean but sophisticated. We would like to reflect both industries on the Title Master Technology and Oil and Gas. We can provide a screen capture of our software if you would like.

Target Market(s)

Oil and Gas Professionals. Various age groups and genders, usually well educated working in Budgeting, Planning, Operations, Finance.

Industry/Entity Type

Software

Requirements
Must have
• Corporate logo and color scheme. RGB 143 Red, 75 Green and 6 Blue. The majority of slides we use are screen captures from our application so we need maximum space. Plus it must be designed to be as small as possible as they are emailed frequently.

```html
<!DOCTYPE html>
<html lang="en">
<head>
<meta charset="utf-8">
<title>Brindlecove Ventures Co. – Slide Master</title>
<link href="https://fonts.googleapis.com/css2?family=Carlito:wght@400;700&family=Questrial&display=swap" rel="stylesheet">
<style>
  :root {
    --brand: #8f4b06;
    --ink: #4a4a4a;
    --ink-strong: #3c3c3c;
    --rule: #c9d3d8;
    --bg-top: #fdfdfd;
    --bg-mid: #f1f1f1;
    --bg-low: #ececec;
    --footer-edge: #111111;
    --white: #ffffff;
    --badge: #6e6e6e;
  }
  * { margin: 0; padding: 0; box-sizing: border-box; }
  html, body { width: 1200px; height: 900px; overflow: hidden; }
  body { font-family: "Carlito", "Calibri", sans-serif; color: var(--ink); }

  .slide {
    position: relative;
    width: 1200px;
    height: 900px;
    overflow: hidden;
    background: linear-gradient(180deg, var(--bg-top) 0%, var(--bg-mid) 55%, var(--bg-low) 100%);
  }
  .slide-texture {
    position: absolute;
    inset: 96px 0 55px 0;
    background: radial-gradient(ellipse at 30% 35%, rgba(0,0,0,0.05), rgba(0,0,0,0) 70%);
  }

  /* Header */
  .header {
    position: absolute;
    left: 0; top: 0;
    width: 1200px; height: 97px;
    border-bottom: 1px solid var(--rule);
  }
  .brand-mark {
    position: absolute;
    left: 42px; top: 6px;
    width: 50px; height: 50px;
    border-radius: 50%;
    background: var(--badge);
  }
  .brand-name {
    position: absolute;
    left: 104px; top: 18px;
    font-family: "Questrial", sans-serif;
    font-size: 18px;
    color: var(--brand);
  }
  .tagline {
    position: absolute;
    left: 132px; top: 60px;
    font-family: "Questrial", sans-serif;
    font-size: 30px;
    color: var(--brand);
    line-height: 1;
  }

  /* Content */
  .section { position: absolute; left: 60px; width: 1000px; }
  .section-head {
    display: flex; align-items: center;
    height: 42px;
  }
  .section-head svg { width: 42px; height: 42px; flex: none; }
  .section-title {
    margin-left: 21px;
    font-size: 25px;
    font-weight: 400;
    color: var(--ink-strong);
  }
  .points { list-style: none; margin-left: 72px; margin-top: 24px; }
  .points li {
    position: relative;
    padding-left: 16px;
    font-size: 19.5px;
    font-weight: 700;
    line-height: 28.5px;
    color: var(--ink);
    margin-bottom: 29px;
  }
  .points li svg {
    position: absolute; left: -1px; top: 8px;
    width: 11px; height: 15px;
  }

  /* Footer */
  .footer {
    position: absolute;
    left: 0; bottom: 0;
    width: 1200px; height: 55px;
    background: var(--brand);
    border-top: 6px solid var(--footer-edge);
    color: var(--white);
  }
  .page-number {
    position: absolute; left: 36px; top: 11px;
    font-size: 21px; font-weight: 700;
  }
  .copyright {
    position: absolute; right: 15px; top: 11px;
    font-family: "Questrial", sans-serif;
    font-size: 22px;
  }
</style>
</head>
<body>
<main class="slide">
  <div class="slide-texture" role="img" aria-label="Soft grey dotted background texture"></div>

  <header class="header">
    <div class="brand-mark"></div>
    <div class="brand-name">Brindlecove Ventures Co.</div>
    <div class="tagline">Connecting Energy Operations</div>
  </header>

  <section class="section" style="top:164px;">
    <div class="section-head">
      <svg viewBox="0 0 42 42" aria-hidden="true">
        <circle cx="21" cy="21" r="19" fill="var(--brand)" stroke="#ffffff" stroke-width="3"/>
        <path d="M12 21h16M22 14l7 7-7 7" fill="none" stroke="#ffffff" stroke-width="3.4" stroke-linecap="round" stroke-linejoin="round"/>
      </svg>
      <h2 class="section-title">Lorem ipsum dolor sit ipsum Lorem ipsum dolor sit ipsum Lorem ipsum</h2>
    </div>
    <ul class="points">
      <li><svg viewBox="0 0 11 15"><path d="M1 1l8 6.5L1 14" fill="none" stroke="#111" stroke-width="3"/></svg>Lorem ipsum dolor sit ipsum Lorem ipsum dolor sit ipsum Lorem ipsum&nbsp; Lorem ipsum dolor<br>sit ipsum Lorem ipsum dolor sit ipsum Lorem ipsum</li>
      <li><svg viewBox="0 0 11 15"><path d="M1 1l8 6.5L1 14" fill="none" stroke="#111" stroke-width="3"/></svg>Lorem ipsum dolor sit ipsum Lorem ipsum dolor sit ipsum Lorem ipsum&nbsp; Lorem ipsum dolor<br>sit ipsum Lorem ipsum dolor sit ipsum Lorem ipsum</li>
      <li><svg viewBox="0 0 11 15"><path d="M1 1l8 6.5L1 14" fill="none" stroke="#111" stroke-width="3"/></svg>Lorem ipsum dolor sit ipsum Lorem ipsum dolor sit ipsum Lorem ipsum&nbsp; Lorem ipsum dolor<br>sit ipsum Lorem ipsum dolor sit ipsum Lorem ipsum</li>
    </ul>
  </section>

  <section class="section" style="top:477px;">
    <div class="section-head">
      <svg viewBox="0 0 42 42" aria-hidden="true">
        <circle cx="21" cy="21" r="19" fill="var(--brand)" stroke="#ffffff" stroke-width="3"/>
        <path d="M12 21h16M22 14l7 7-7 7" fill="none" stroke="#ffffff" stroke-width="3.4" stroke-linecap="round" stroke-linejoin="round"/>
      </svg>
      <h2 class="section-title">Lorem ipsum dolor sit ipsum Lorem ipsum dolor sit ipsum Lorem ipsum</h2>
    </div>
    <ul class="points">
      <li><svg viewBox="0 0 11 15"><path d="M1 1l8 6.5L1 14" fill="none" stroke="#111" stroke-width="3"/></svg>Lorem ipsum dolor sit ipsum Lorem ipsum dolor sit ipsum Lorem ipsum&nbsp; Lorem ipsum dolor<br>sit ipsum Lorem ipsum dolor sit ipsum Lorem ipsum</li>
      <li><svg viewBox="0 0 11 15"><path d="M1 1l8 6.5L1 14" fill="none" stroke="#111" stroke-width="3"/></svg>Lorem ipsum dolor sit ipsum Lorem ipsum dolor sit ipsum Lorem ipsum&nbsp; Lorem ipsum dolor<br>sit ipsum Lorem ipsum dolor sit ipsum Lorem ipsum</li>
      <li><svg viewBox="0 0 11 15"><path d="M1 1l8 6.5L1 14" fill="none" stroke="#111" stroke-width="3"/></svg>Lorem ipsum dolor sit ipsum Lorem ipsum dolor sit ipsum Lorem ipsum&nbsp; Lorem ipsum dolor<br>sit ipsum Lorem ipsum dolor sit ipsum Lorem ipsum</li>
    </ul>
  </section>

  <footer class="footer">
    <div class="page-number">Page : 01</div>
    <div class="copyright">Copyright text here</div>
  </footer>
</main>
</body>
</html>
```